Relunaro layout redesign brief

Relunaro.example is a functional site developed in Ruby on Rails for which we wish to overhaul the layout and overall design concepts. New page designs must incorporate the existing functionality and work flows and allow the user interactions already defined.

Redesign of the primary logo is not included in the brief.

The objective of Relunaro is to provide an holistic approach to developing a healthy lifestyle including diet, exercise and mental well-being by providing a series of tools and interactions. All three elements must be included

The designer must demonstrate that they have utilised the site in order to gain an understanding of the various component available. RelunAro needs multiple levels of engagement, needs to be responsive, along the lines to allow the users to anticipate the opportunity of becoming a member. We need to be able to display synopsis of members blogs, successes and other news items as we see fit on the landing page.

Target Market(s)

Aimed at 18-65 male and female with an interest in changing their lifestyle to be healthier, fitter and a stronger confidence in their self-image. This site is about taking personal responsibility of your own life using the emotional support available through the tools and interactions within the site.

Requirements
Must have
• Must have the relunaro logo.
Must retain the sections (though not necessarily the names of the sections)
Make use of colours, graphics and images.
Appropriate use of popup overlays for providing help and support.
Community features
Space for advertisers

```html
<!DOCTYPE html>
<html lang="en">
<head>
<meta charset="utf-8">
<title>RelunAro – Be fitter, be healthier, be in control</title>
<link rel="stylesheet" href="https://fonts.googleapis.com/css2?family=Open+Sans:wght@400;600&family=Didact+Gothic&display=swap">
<style>
:root{
  --green:#8cc32e;
  --green-dark:#76a823;
  --ink:#333333;
  --text:#4a4a4a;
  --grey-btn:#6d6d6d;
  --band:#efefef;
  --footer:#2b2b2b;
  --footer-text:#b5b5b5;
  --frame:#d6d6d6;
}
*{margin:0;padding:0;box-sizing:border-box}
html,body{width:988px;height:1200px;overflow:hidden;background:#fff}
body{position:relative;font-family:"Open Sans",Arial,sans-serif;color:var(--text)}
.abs{position:absolute}

/* header */
.brand{left:155px;top:26px;display:flex;align-items:center;gap:8px;font-family:"Didact Gothic","Open Sans",sans-serif;font-size:25px;color:var(--green)}
.brand-dot{width:14px;height:14px;border-radius:50%;background:var(--green)}
.sign-in{left:750px;top:28px;width:71px;height:26px;background:var(--grey-btn);border-radius:3px;color:#fff;font-size:10px;font-weight:600;display:flex;align-items:center;justify-content:center}

.main-nav{left:152px;top:78px;width:685px;height:35px;background:var(--green);border:1px solid var(--green-dark);box-shadow:inset 0 0 0 2px #a2d14a}
.main-nav a{position:absolute;top:12px;color:#fff;font-size:8.5px;text-decoration:none;letter-spacing:.1px}
.main-nav .sep{position:absolute;top:6px;width:1px;height:22px;background:#a9d45c}

/* hero */
.hero{left:152px;top:127px;width:685px;height:222px;border:1px solid var(--frame);padding:2px;background:#fff}
.hero-photo{width:100%;height:100%;background:linear-gradient(90deg,#e9e9e9 0%,#dfe3dc 20%,#7fb93a 32%,#eee8ea 50%,#e85fb6 62%,#f3c7e3 78%,#e4ecf2 100%)}
.hero-title{left:590px;top:147px;font-family:"Didact Gothic",sans-serif;font-size:27px;color:#333}
.hero-tag{left:590px;top:184px;font-family:"Didact Gothic",sans-serif;font-size:14px;color:#444}
.hero-cta{left:583px;top:216px;width:115px;height:36px;background:var(--green);color:#fff;font-family:"Didact Gothic",sans-serif;font-size:13.5px;display:flex;align-items:center;padding-left:15px;gap:10px}
.dots{left:162px;top:334px;display:flex;gap:3px}
.dots span{width:6px;height:6px;border-radius:50%;background:#555}
.dots span:first-child{background:var(--green)}

/* headings */
.sec-title{font-size:16.5px;color:var(--ink);font-weight:400}
.sec-title em{font-style:normal;color:var(--green)}
.dotline{height:5px;background-image:radial-gradient(#c8c8c8 0.7px,transparent 0.8px);background-size:2px 2px}

.photo{border:1px solid var(--frame);padding:2px;background:#fff}
.photo div{width:100%;height:100%}
.body-text{font-size:8.5px;line-height:14px;color:var(--text)}
.justify{text-align:justify}

.read-more{display:flex;height:16px;font-family:Arial,sans-serif;font-size:8.5px;color:#fff}
.read-more span{background:var(--grey-btn);width:64px;display:flex;align-items:center;justify-content:center}
.read-more i{width:16px;background:var(--green);display:flex;align-items:center;justify-content:center}

.band{left:0;top:514px;width:988px;height:288px;background:var(--band)}

/* footer */
.footer{left:0;top:1135px;width:988px;height:65px;background:var(--footer);border-top:4px solid var(--green)}
.footer-text{font-size:8.5px;color:var(--footer-text)}
.social{left:736px;top:1162px;display:flex;gap:7px}
.social span{width:14px;height:14px;border:1px solid #666}
</style>
</head>
<body>

<header>
  <div class="abs brand"><span class="brand-dot"></span>RelunAro</div>
  <a class="abs sign-in">SIGN IN</a>
  <nav class="abs main-nav">
    <a style="left:24px">HOME</a><span class="sep" style="left:72px"></span>
    <a style="left:89px">ABOUT US</a><span class="sep" style="left:155px"></span>
    <a style="left:173px">SERVICES</a><span class="sep" style="left:224px"></span>
    <a style="left:240px">ARTICLES</a><span class="sep" style="left:289px"></span>
    <a style="left:317px">Q&amp;A</a><span class="sep" style="left:362px"></span>
    <a style="left:384px">PRIVACY POLICY</a><span class="sep" style="left:465px"></span>
    <a style="left:487px">CONTACT US</a>
  </nav>
</header>

<section>
  <div class="abs hero"><div class="hero-photo" role="img" aria-label="Green apple wrapped in a measuring tape beside pink dumbbells, a towel and a water bottle"></div></div>
  <div class="abs hero-title">RelunAro</div>
  <div class="abs hero-tag">Be fitter, be healthier, be in control</div>
  <a class="abs hero-cta">Get Started
    <svg width="9" height="14" viewBox="0 0 9 14"><path d="M1.5 1.5 7 7l-5.5 5.5" fill="none" stroke="#fff" stroke-width="2.2"/></svg></a>
  <div class="abs dots"><span></span><span></span><span></span><span></span></div>
</section>

<section>
  <h2 class="abs sec-title" style="left:153px;top:370px">Welcome to <em>RelunAro</em></h2>
  <div class="abs dotline" style="left:314px;top:381px;width:522px"></div>
  <div class="abs photo" style="left:152px;top:409px;width:120px;height:78px"><div role="img" aria-label="Smiling woman holding a dumbbell beside fresh fruit and vegetables" style="background:linear-gradient(90deg,#e8e4df,#c9a98c 40%,#8fbf4a 70%,#e8623a)"></div></div>
  <p class="abs body-text justify" style="left:285px;top:411px;width:551px">At RelunAro we are committed to helping people reach their weight and health goals. Our aim is to empower people of all ages, shapes and abilities to re-evaluate their relationships and underlying experiences with food, self-perception and lifestyle. We offer nutrition, health, and fitness tools, support, and resources that are 100% free and help the transition to a permanent, healthy lifestyle. Far beyond just weight loss! RelunAro helps everyone learn to eat better and exercise regularly—for life. And even if you simply want to stay in shape, you can still join and benefit from RelunAro tools, resources and community features.</p>
</section>

<section>
  <div class="abs band"></div>

  <h2 class="abs sec-title" style="left:153px;top:540px">Record</h2>
  <div class="abs photo" style="left:152px;top:577px;width:120px;height:97px"><div role="img" aria-label="Red apple wrapped in a measuring tape" style="background:radial-gradient(circle at 50% 45%,#d8282a 0 28%,#f4f4f4 30%)"></div></div>
  <p class="abs body-text justify" style="left:153px;top:688px;width:154px;line-height:12.8px">Record and view your personal data, your mood and emotions, your food intake, your activity and your weight and measurements. Choose your personalised RelunAroVital.</p>
  <a class="abs read-more" style="left:153px;top:772px"><span>Read More</span><i><svg width="10" height="9" viewBox="0 0 10 9"><path d="M0 4.5h8M5 1l3.5 3.5L5 8" fill="none" stroke="#fff" stroke-width="1.8"/></svg></i></a>

  <h2 class="abs sec-title" style="left:324px;top:540px">Tools</h2>
  <div class="abs photo" style="left:328px;top:577px;width:120px;height:97px"><div role="img" aria-label="Child stretching over a pink exercise ball" style="background:radial-gradient(circle at 55% 60%,#f04e8a 0 25%,#9fa7e6 27%)"></div></div>
  <p class="abs body-text justify" style="left:328px;top:688px;width:154px;line-height:12.8px">At RelunAro we have developed a unique set of RelunAroVital tools for you to use and incorporate into your daily routines. They will enable you to create a plan.</p>
  <a class="abs read-more" style="left:326px;top:772px"><span>Read More</span><i><svg width="10" height="9" viewBox="0 0 10 9"><path d="M0 4.5h8M5 1l3.5 3.5L5 8" fill="none" stroke="#fff" stroke-width="1.8"/></svg></i></a>

  <h2 class="abs sec-title" style="left:504px;top:540px">Goals</h2>
  <div class="abs photo" style="left:506px;top:577px;width:120px;height:97px"><div role="img" aria-label="Waist measured with a tape" style="background:linear-gradient(180deg,#f2f2f2 0 30%,#c99c7e 45%,#8e9aa6 80%)"></div></div>
  <p class="abs body-text justify" style="left:508px;top:688px;width:155px;line-height:12.8px">Keep track of your goals on your personalised Dashboard, create new goals and see patterns in your behaviour whether it is around food, emotions, activity or other.</p>
  <a class="abs read-more" style="left:509px;top:772px"><span>Read More</span><i><svg width="10" height="9" viewBox="0 0 10 9"><path d="M0 4.5h8M5 1l3.5 3.5L5 8" fill="none" stroke="#fff" stroke-width="1.8"/></svg></i></a>

  <h2 class="abs sec-title" style="left:680px;top:540px">Get Healthy</h2>
  <div class="abs photo" style="left:681px;top:577px;width:120px;height:97px"><div role="img" aria-label="Fresh mixed salad with tomatoes and onion" style="background:linear-gradient(135deg,#b7dd8a,#4c9a2a 50%,#d8423a 75%,#eef2f4)"></div></div>
  <p class="abs body-text justify" style="left:683px;top:688px;width:155px;line-height:12.8px">Record, track and monitor your progress to help you create your healthier life. Be informed with health news and updates from our informative blogs and articles.</p>
  <a class="abs read-more" style="left:681px;top:772px"><span>Read More</span><i><svg width="10" height="9" viewBox="0 0 10 9"><path d="M0 4.5h8M5 1l3.5 3.5L5 8" fill="none" stroke="#fff" stroke-width="1.8"/></svg></i></a>
</section>

<section>
  <h2 class="abs sec-title" style="left:153px;top:840px">Latest Articles</h2>

  <div class="abs photo" style="left:152px;top:880px;width:154px;height:82px"><div role="img" aria-label="Rolled pancakes in a frying pan" style="background:linear-gradient(160deg,#f5f5f5 0 20%,#2a2a2a 35%,#d9a65a 55%,#2a2a2a 80%,#f2f2f2)"></div></div>
  <h3 class="abs" style="left:320px;top:881px;font-size:12.5px;font-weight:400;color:var(--ink)">Shrove Tuesday 65 calorie Pancakes</h3>
  <p class="abs body-text justify" style="left:320px;top:916px;width:241px;line-height:13.5px">Pellentesque habitant morbi tristique senectus et netus et malesuada fames ac turpis egestas. Vestibulum tortor. Pellentesque habitant morbi tristique senectus et netus et malesuada.</p>

  <div class="abs photo" style="left:152px;top:986px;width:154px;height:82px"><div role="img" aria-label="Raspberries spilling from a striped paper cup" style="background:linear-gradient(135deg,#f4dada,#d8283c 50%,#f2e6e6)"></div></div>
  <h3 class="abs" style="left:320px;top:987px;font-size:12.5px;font-weight:400;color:var(--ink)">Salmon &amp; Asparagus Salad with Raspberries</h3>
  <p class="abs body-text justify" style="left:320px;top:1022px;width:241px;line-height:13.5px">Pellentesque habitant morbi tristique senectus et netus et malesuada fames ac turpis egestas. Vestibulum tortor. Pellentesque habitant morbi tristique senectus et netus et malesuada.</p>

  <a class="abs read-more" style="left:153px;top:1093px"><span>Read More</span><i><svg width="10" height="9" viewBox="0 0 10 9"><path d="M0 4.5h8M5 1l3.5 3.5L5 8" fill="none" stroke="#fff" stroke-width="1.8"/></svg></i></a>
</section>

<aside>
  <h2 class="abs sec-title" style="left:596px;top:840px">Community</h2>
  <div class="abs dotline" style="left:700px;top:849px;width:137px"></div>

  <div class="abs photo" style="left:597px;top:883px;width:43px;height:39px"><div role="img" aria-label="Dumbbells, water bottle and an apple" style="background:linear-gradient(135deg,#eef2f5,#9fb4c4 50%,#7cbf3a)"></div></div>
  <p class="abs body-text" style="left:651px;top:882px;width:186px;line-height:12.8px">Donec luctus nisl in nibh ultricies quis convallis justo convallis. Fusce mattis mauris id enim justo convallis Fusce .</p>

  <div class="abs photo" style="left:597px;top:941px;width:43px;height:39px"><div role="img" aria-label="Bowl of mixed fruit" style="background:linear-gradient(135deg,#f4b13a,#d8343a 50%,#6fb03a)"></div></div>
  <p class="abs body-text justify" style="left:651px;top:939px;width:186px;line-height:12.8px">Convallis. Fusce mattis mauris id enim. Magnust nibhjusto convallis. Fusce mattis mauris id enim.</p>

  <div class="abs photo" style="left:597px;top:1000px;width:43px;height:39px"><div role="img" aria-label="Woman holding fresh vegetables" style="background:linear-gradient(180deg,#e6dcd2,#b8875f 50%,#78b23c)"></div></div>
  <p class="abs body-text" style="left:651px;top:997px;width:186px;line-height:12.8px">Convallis. Fusce justo convallis. Fusce mattis mauris id enim.mattis mauris id enim. Magnust nibh dolorest onlso at quist mattiest.</p>

  <a class="abs read-more" style="left:757px;top:1063px"><span>Read More</span><i><svg width="10" height="9" viewBox="0 0 10 9"><path d="M0 4.5h8M5 1l3.5 3.5L5 8" fill="none" stroke="#fff" stroke-width="1.8"/></svg></i></a>
</aside>

<footer>
  <div class="abs footer"></div>
  <p class="abs footer-text" style="left:153px;top:1154px">© Copyright Orvane Labs Ltd. 2014</p>
  <p class="abs footer-text" style="left:153px;top:1173px">About Us &nbsp;|&nbsp; Contact Us &nbsp;|&nbsp; Terms and Conditions &nbsp;|&nbsp; Privacy Policy &nbsp;|&nbsp; Unsubscribe from newsletter</p>
  <div class="abs social"><span></span><span></span><span></span><span></span><span></span></div>
</footer>

</body>
</html>
```